Business Card Design

I need a card design for Melbourne based business in Australia, called M P Concrete Services. We Concrete and excavate. Concreteing is main part of business.Commercial ,Residential and industrial.We want to be known as M P C (services) as form of abbreviation.We would like to highlight the initials with contact phone. A clean straight edge design. We have no color preference and would prefer a design that can easily be used on all parts of our business including clothing,vechiles and stationary

Industry/Entity Type

Business

Contact Information for Business Card

Hugh 0491 570 156
Peter 0491 570 157
mpcsercices@quollmail.com

```html
<!DOCTYPE html>
<html lang="en">
<head>
<meta charset="utf-8">
<title>M P Concrete Services – Business Card</title>
<link href="https://fonts.googleapis.com/css2?family=Questrial&display=swap" rel="stylesheet">
<style>
  :root {
    --page-bg: #e6e6e6;
    --card-light: #6a6a6c;
    --card-dark: #404042;
    --band: #1d1b1d;
    --side-bar: #1a1a1a;
    --mark-text: #c8c8ca;
    --name-text: #a4a4a6;
    --contact-text: #d2d2d4;
    --band-text: #8e8e90;
  }
  html, body {
    margin: 0;
    width: 1200px;
    height: 799px;
    overflow: hidden;
    background: var(--page-bg);
    font-family: "Questrial", "Century Gothic", sans-serif;
  }
  .card {
    position: absolute;
    left: 150px;
    top: 125px;
    width: 900px;
    height: 550px;
    box-shadow: 0 10px 30px rgba(0,0,0,0.25);
    overflow: hidden;
  }
  .card-art {
    position: absolute;
    inset: 0;
  }
  .brand {
    position: absolute;
    top: 120px;
    left: 0;
    width: 100%;
    text-align: center;
  }
  .brand-initials {
    display: block;
    color: var(--mark-text);
    font-size: 92px;
    letter-spacing: 6px;
    line-height: 1;
  }
  .brand-name {
    display: block;
    margin-top: 10px;
    color: var(--name-text);
    font-size: 24px;
    letter-spacing: 0.5px;
  }
  .contacts {
    position: absolute;
    top: 280px;
    left: 0;
    width: 100%;
    text-align: center;
    color: var(--contact-text);
    font-size: 26px;
    line-height: 1.3;
  }
  .contacts p { margin: 0; }
  .band-name {
    position: absolute;
    bottom: 28px;
    left: 0;
    width: 100%;
    text-align: center;
    color: var(--band-text);
    font-size: 25px;
    letter-spacing: 0.5px;
  }
</style>
</head>
<body>
  <div class="card">
    <svg class="card-art" width="900" height="550" viewBox="0 0 900 550">
      <defs>
        <radialGradient id="cardGlow" cx="50%" cy="38%" r="70%">
          <stop offset="0" stop-color="#6e6e70"/>
          <stop offset="1" stop-color="#3e3e40"/>
        </radialGradient>
      </defs>
      <rect class="card-face" width="900" height="550" fill="url(#cardGlow)"/>
      <path class="card-band" d="M0 395 Q450 515 900 395 L900 550 L0 550 Z" fill="var(--band)"/>
      <rect class="side-bar-left" x="0" y="150" width="14" height="260" fill="var(--side-bar)"/>
      <rect class="side-bar-right" x="886" y="150" width="14" height="260" fill="var(--side-bar)"/>
    </svg>

    <div class="brand">
      <span class="brand-initials">M P C</span>
      <span class="brand-name">M P Concrete Services</span>
    </div>

    <div class="contacts">
      <p>Hugh 0491 570 156</p>
      <p>Peter 0491 570 157</p>
      <p>mpcsercices@quollmail.com</p>
    </div>

    <div class="band-name">M P Concrete Services</div>
  </div>
</body>
</html>
```